Up to the Challenge? Canadian based consulting company needs a two sided business card design

A Canadian based security risk management consulting company needs a two-sided business card design. What we do is provide advice and guidance related to emergency, security and business continuity management for small, medium and large companies to help ensure the protection of their people, assets, information, services, operations and reputation.

The final design should be simple, only one or two colours, eye catching, professional and one that makes people look at three or more times just because it looks so darn good.

I have include examples of business cards I like.

Target Market(s)

Small, medium and large companies.

Industry/Entity Type

Security

Contact Information for Business Card

Business Card Size: Standard size of 3.5" (89mm) x 2.0" (51mm) - (see full specifications and guides on PRINTA's website if required)
Card Stock: Looking to use PRINTA's Velda 32pt stock textured paper - seam colour either chili red or black
Business Name: The Harrowfield Group
Website: www.theharrowfieldgroup.example
Telephone: (555)214-0397
Name: Dana Forsythe
Position: Principle
e-mail: Dana.Forsythe@theharrowfieldgroup.example

Font styles to use
Serif

Colors
ec1f27
000000
9d9d9d
aaaaaa
606060

Requirements
Must have
• - "The Harrowfield Group" logo (see uploaded files). I have included grey scale and colour versions.
• - Business card details (as above)
Nice to have
• - One side black or grey scale.
• - Other side would likely be white.
• - Everyone likes the silver logo on the black background.
• - Small element of colour i.e. red but I'm leaning more to greyscale.
Should not have
• - A lot of colour. Keep it simple.

```html
<!DOCTYPE html>
<html lang="en">
<head>
<meta charset="utf-8">
<title>The Harrowfield Group — Business Card</title>
<link rel="stylesheet" href="https://fonts.googleapis.com/css2?family=PT+Serif:wght@400;700&display=swap">
<style>
  :root {
    --red: #ec1f27;
    --black: #000000;
    --silver: #aaaaaa;
    --grey-light: #9d9d9d;
    --grey-dark: #606060;
    --ink: #3a3a3a;
    --paper: #ffffff;
    --backdrop: #e4e4e4;
  }
  * { margin: 0; padding: 0; box-sizing: border-box; }
  html, body {
    width: 1200px;
    height: 1000px;
    overflow: hidden;
    background: var(--backdrop);
    font-family: "PT Serif", Georgia, serif;
  }
  .sheet {
    width: 1200px;
    height: 1000px;
    display: flex;
    flex-direction: column;
    align-items: center;
    justify-content: space-evenly;
  }
  .card {
    position: relative;
    width: 700px;
    height: 400px;
    box-shadow: 0 6px 18px rgba(0,0,0,0.18);
  }

  /* Front: contact side */
  .card--front { background: var(--paper); }
  .brand-mark {
    position: absolute;
    left: 60px;
    top: 62px;
    display: flex;
    align-items: center;
    gap: 14px;
  }
  .brand-mark__square {
    width: 34px;
    height: 34px;
    background: var(--red);
  }
  .brand-mark__name {
    font-size: 17px;
    font-weight: 400;
    color: var(--grey-dark);
    letter-spacing: 0.04em;
  }
  .identity {
    position: absolute;
    left: 330px;
    top: 128px;
  }
  .identity__name {
    font-size: 36px;
    font-weight: 700;
    color: var(--grey-dark);
    line-height: 1.05;
  }
  .identity__role {
    font-size: 26px;
    font-weight: 400;
    color: var(--grey-light);
    line-height: 1.2;
  }
  .contact {
    position: absolute;
    left: 60px;
    top: 240px;
    list-style: none;
    font-size: 20px;
    line-height: 1.45;
    color: var(--ink);
  }

  /* Back: brand side */
  .card--back {
    background: var(--black);
    display: flex;
    align-items: center;
    justify-content: center;
    gap: 36px;
  }
  .wordmark {
    text-align: center;
    color: var(--silver);
    font-weight: 400;
    text-transform: uppercase;
    line-height: 1.15;
  }
  .wordmark__main {
    display: block;
    font-size: 42px;
    letter-spacing: 0.08em;
  }
  .wordmark__sub {
    display: block;
    font-size: 30px;
    letter-spacing: 0.3em;
  }
  .wordmark-square {
    width: 56px;
    height: 56px;
    background: var(--silver);
  }
</style>
</head>
<body>
  <main class="sheet">
    <section class="card card--front" aria-label="Business card, contact side">
      <div class="brand-mark">
        <span class="brand-mark__square"></span>
        <span class="brand-mark__name">The Harrowfield Group</span>
      </div>
      <div class="identity">
        <h1 class="identity__name">Dana Forsythe</h1>
        <p class="identity__role">Principle</p>
      </div>
      <ul class="contact">
        <li>Dana.Forsythe@theharrowfieldgroup.example</li>
        <li>(555) 214-0397</li>
        <li>www.theharrowfieldgroup.example</li>
      </ul>
    </section>

    <section class="card card--back" aria-label="Business card, brand side">
      <p class="wordmark">
        <span class="wordmark__main">The Harrowfield</span>
        <span class="wordmark__sub">Group</span>
      </p>
      <span class="wordmark-square"></span>
    </section>
  </main>
</body>
</html>
```